Illustration Style Book Cover for Business Book

I have written a book called "The Corner Shop Keeper's Handbook". The title should be self-explanatory. It's a how-to for the owner or manager of a small business on a variety of subjects like makreting, operations, finance, managing people, etc.
I have no pre-defined notions about what i want this to look like and I would like the designer to take full creative license. The "owners manual" concept should come through in the design.

Target Market(s)

Small Business Owners and Operators

Industry/Entity Type

All - Small business

Font styles to use
Sans Serif

Colors

Designer to choose colors to be used in the design.

Requirements
Nice to have
• Should look like an “owners manual"
Should not have
• Photos

```html
<!DOCTYPE html>
<html lang="en">
<head>
<meta charset="utf-8">
<title>The Corner Shop Keeper's Handbook</title>
<link href="https://fonts.googleapis.com/css2?family=Barlow+Condensed:wght@300;800&display=swap" rel="stylesheet">
<style>
  :root {
    --mint: #55ffc5;
    --ink: #000000;
    --paper: #ffffff;
    --pink: #ff2a85;
    --yellow: #ffdc2a;
    --navy: #154e8a;
    --orange: #ff4e03;
  }
  html, body {
    margin: 0;
    padding: 0;
    width: 840px;
    height: 1200px;
    overflow: hidden;
    background: var(--mint);
  }
  .cover {
    position: relative;
    width: 840px;
    height: 1200px;
    background: var(--mint);
    overflow: hidden;
  }
  .cover-art {
    position: absolute;
    inset: 0;
    width: 840px;
    height: 1200px;
  }
  .title-bold {
    font-family: "Barlow Condensed", sans-serif;
    font-weight: 800;
    fill: var(--ink);
  }
  .title-light {
    font-family: "Barlow Condensed", sans-serif;
    font-weight: 300;
    fill: var(--paper);
  }
  .bracket { fill: none; stroke: var(--paper); stroke-width: 4; }
  .chart-stop-pink { stop-color: var(--pink); }
  .chart-stop-ink { stop-color: var(--ink); }
  .chart-stop-yellow { stop-color: var(--yellow); }
  .chart-stop-navy { stop-color: var(--navy); }
  .chart-stop-orange { stop-color: var(--orange); }
  .chart-fade-mint { stop-color: var(--mint); }
</style>
</head>
<body>
<main class="cover">
  <svg class="cover-art" viewBox="0 0 840 1200" xmlns="http://www.w3.org/2000/svg">
    <title>The Corner Shop Keeper's Handbook</title>
    <defs>
      <linearGradient id="chart-tones" x1="0" y1="0" x2="1" y2="0">
        <stop offset="0" class="chart-stop-pink" />
        <stop offset="0.3" class="chart-stop-ink" />
        <stop offset="0.5" class="chart-stop-yellow" />
        <stop offset="0.7" class="chart-stop-navy" />
        <stop offset="1" class="chart-stop-orange" />
      </linearGradient>
      <linearGradient id="chart-fade" x1="0" y1="0" x2="0" y2="1">
        <stop offset="0" class="chart-fade-mint" stop-opacity="0.75" />
        <stop offset="0.35" class="chart-fade-mint" stop-opacity="0" />
      </linearGradient>
    </defs>

    <polyline class="bracket" points="107,430 107,113 350,113" />

    <g class="title">
      <text class="title-bold" x="174" y="292" font-size="142" textLength="528" lengthAdjust="spacingAndGlyphs">THE CORNER</text>
      <text class="title-bold" x="178" y="430" font-size="162">SHOP</text>
      <text class="title-light" x="178" y="562" font-size="146">KEEPER'S</text>
      <text class="title-light" x="178" y="700" font-size="146">HANDBOOK</text>
    </g>

    <g class="growth-illustration" role="img" aria-label="Colourful rising bar chart with an upward trend arrow">
      <rect x="0" y="716" width="840" height="484" fill="url(#chart-tones)" />
      <rect x="0" y="716" width="840" height="484" fill="url(#chart-fade)" />
    </g>
  </svg>
</main>
</body>
</html>
```